bottle label design for a cultured milk based product

(Edit : name of the company is Qeshari . The bottle will be see through )
Edit 2 :I noticed people only sending a logo this isn't what I want please read the description

I'm starting a small dairy company for cultured milk products .

1. I need a logo
2.i need a design for the bottle label
3. I need a design for the bottle it's self

As a professional suggest for me the sizes for large medium and small (ie 1.5 liter) .

We are still brainstorming this but hope you can help us how it will be designed

The main theme behind it is as follows
Camel based milk
Cultured/fermented/probiotic milk
Fenugreek added to enhance flavour
Organic
Plant based biodegradable bottle (eco-friendly)
(Shake before use)

This must be a full label which also includes the nutritional break down table but keep it empty for us to fill in

Since on the bigger bottles has more space and I thought we could add a small story since cultured milk is part of our history (united Arab Emirates)

The idea of how the label would look like is that it can have a small outline of a camel and a brown background of sand dunes and the font would be in white but you can ignore all of this and show us what you can think of

If we have missed something , as a professional guide us .

```html
<!DOCTYPE html>
<html lang="en">
<head>
<meta charset="UTF-8">
<title>Qeshari – Camel Milk Label Range</title>
<link rel="stylesheet" href="https://fonts.googleapis.com/css2?family=Fredoka:wght@600;700&family=Josefin+Sans:wght@400;600;700&display=swap">
<style>
  :root {
    --page: #ffffff;
    --label-white: #ffffff;
    --cocoa: #5a4840;
    --sand: #e2a66c;
    --ocean: #2d4fa6;
    --ocean-deep: #1d3378;
    --sun: #f1b434;
    --foam: #ffffff;
    --edge: #e7e3df;
  }
  * { margin: 0; padding: 0; box-sizing: border-box; }
  html, body { width: 1200px; height: 1200px; overflow: hidden; background: var(--page); }
  .range { position: relative; width: 1200px; height: 1200px; }

  .label {
    position: absolute;
    overflow: hidden;
    background: var(--label-white);
    box-shadow: 0 0 0 1px var(--edge), 0 14px 30px rgba(0,0,0,0.08);
    text-align: center;
  }
  .label__shapes { position: absolute; inset: 0; width: 100%; height: 100%; }
  .label__content { position: absolute; inset: 0; }

  .badge {
    position: absolute;
    border-radius: 50%;
    width: 30px; height: 30px;
  }

  .camel-art {
    position: absolute;
    left: 50%;
    transform: translateX(-50%);
    border-radius: 6px;
  }

  /* Qeshari label */
  .label--qeshari { left: 60px; top: 385px; width: 340px; height: 430px; }
  .label--qeshari .badge { right: 12px; top: 18px; background: var(--label-white); border: 2px solid var(--cocoa); }
  .label--qeshari .camel-art { top: 108px; width: 112px; height: 78px; background: var(--cocoa); }
  .qeshari__name {
    position: absolute; left: 0; right: 0; top: 200px;
    font-family: "Fredoka", sans-serif; font-weight: 700; font-size: 52px; line-height: 1.1; letter-spacing: 1px;
    color: var(--cocoa);
  }
  .qeshari__tagline {
    position: absolute; left: 0; right: 0; top: 280px;
    font-family: "Fredoka", sans-serif; font-weight: 700; font-size: 21px; line-height: 1.15;
    color: var(--cocoa); text-transform: uppercase; letter-spacing: 0.5px;
  }
  .qeshari__volume {
    position: absolute; left: 8px; top: 362px;
    font-family: "Fredoka", sans-serif; font-weight: 600; font-size: 11px; color: var(--cocoa);
  }
  .qeshari__note {
    position: absolute; left: 50%; top: 380px; transform: translateX(-50%);
    background: var(--cocoa); color: var(--label-white);
    font-family: "Josefin Sans", sans-serif; font-size: 9.5px;
    padding: 4px 18px 3px; border-radius: 10px; white-space: nowrap;
  }

  /* Fermented label */
  .label--fermented { left: 425px; top: 340px; width: 350px; height: 520px; }
  .label--fermented .badge { right: 16px; top: 16px; background: var(--label-white); }
  .label--fermented .camel-art { top: 100px; width: 170px; height: 82px; background: var(--sand); }
  .fermented__rule { position: absolute; left: 88px; right: 88px; top: 192px; height: 1.5px; background: var(--sand); }
  .fermented__kicker {
    position: absolute; left: 0; right: 0; top: 201px;
    font-family: "Josefin Sans", sans-serif; font-size: 10px; letter-spacing: 3px;
    color: var(--sand); text-transform: uppercase;
  }
  .fermented__name {
    position: absolute; left: 0; right: 0; top: 228px;
    font-family: "Josefin Sans", sans-serif; font-weight: 600; font-size: 80px; line-height: 1;
    color: var(--sand);
  }
  .fermented__type {
    position: absolute; left: 0; right: 0; top: 331px;
    font-family: "Josefin Sans", sans-serif; font-weight: 400; font-size: 22px; line-height: 1.1; letter-spacing: 2px;
    color: var(--sand); text-transform: uppercase;
  }
  .fermented__type-rule { position: absolute; left: 66px; right: 66px; height: 1.5px; background: var(--sand); }
  .fermented__type-rule--above { top: 322px; }
  .fermented__type-rule--below { top: 360px; }
  .fermented__note {
    position: absolute; left: 0; right: 0; top: 378px;
    font-family: "Josefin Sans", sans-serif; font-size: 12.5px;
    color: var(--sand);
  }
  .fermented__volume {
    position: absolute; left: 8px; top: 396px;
    font-family: "Josefin Sans", sans-serif; font-size: 10px; color: var(--cocoa);
  }

  /* Organic blue label */
  .label--organic {
    left: 800px; top: 385px; width: 340px; height: 430px;
    background: linear-gradient(180deg, var(--ocean) 0%, var(--ocean-deep) 100%);
  }
  .label--organic .badge { right: 12px; top: 16px; background: var(--foam); border: 2px solid var(--ocean); }
  .label--organic .camel-art { top: 48px; width: 98px; height: 76px; background: var(--sun); }
  .organic__name {
    position: absolute; left: 0; right: 0; top: 138px;
    font-family: "Josefin Sans", sans-serif; font-weight: 600; font-size: 58px; line-height: 1;
    color: var(--foam);
  }
  .organic__tagline {
    position: absolute; left: 0; right: 0; top: 208px;
    font-family: "Josefin Sans", sans-serif; font-weight: 700; font-size: 13.5px; letter-spacing: 0.5px;
    color: var(--foam); text-transform: uppercase;
  }
  .organic__splash {
    position: absolute; left: 50%; top: 245px; transform: translateX(-50%);
    width: 250px; height: 80px; border-radius: 50%;
    background: radial-gradient(ellipse at center, rgba(255,255,255,0.95) 0%, rgba(255,255,255,0.55) 45%, rgba(255,255,255,0) 72%);
  }
  .organic__note {
    position: absolute; left: 0; right: 0; top: 350px;
    font-family: "Josefin Sans", sans-serif; font-size: 10.5px; color: var(--foam);
  }
  .organic__volume {
    position: absolute; left: 0; right: 0; top: 372px;
    font-family: "Josefin Sans", sans-serif; font-weight: 600; font-size: 17px; color: var(--foam);
  }
</style>
</head>
<body>
<main class="range">

  <section class="label label--qeshari">
    <svg class="label__shapes" viewBox="0 0 340 430" preserveAspectRatio="none" aria-hidden="true">
      <path fill="var(--cocoa)" d="M0 0 H120 C112 18 96 26 78 30 C54 36 44 52 34 70 C24 86 12 92 0 94 Z"/>
      <path fill="var(--cocoa)" d="M340 0 H232 C244 16 258 22 276 26 C296 30 312 42 322 60 C328 70 334 74 340 76 Z"/>
    </svg>
    <div class="label__content">
      <span class="badge"></span>
      <div class="camel-art" role="img" aria-label="Brown silhouette of a walking camel"></div>
      <h1 class="qeshari__name">QESHARI</h1>
      <p class="qeshari__tagline">Organic camel<br>based milk</p>
      <span class="qeshari__volume">1.5 L</span>
      <p class="qeshari__note">Fenugreek added to enhance flavour</p>
    </div>
  </section>

  <section class="label label--fermented">
    <svg class="label__shapes" viewBox="0 0 350 520" preserveAspectRatio="none" aria-hidden="true">
      <path fill="var(--sand)" d="M350 0 H282 C276 22 262 38 264 60 C266 84 290 92 312 84 C330 78 342 88 350 96 Z"/>
      <path fill="var(--sand)" d="M0 520 V420 C16 412 36 414 52 422 C72 432 96 436 118 446 C140 458 132 490 112 520 Z"/>
    </svg>
    <div class="label__content">
      <span class="badge"></span>
      <div class="camel-art" role="img" aria-label="Tan silhouette of a mother camel walking with her calf"></div>
      <span class="fermented__rule"></span>
      <p class="fermented__kicker">Camel based milk</p>
      <h2 class="fermented__name">Laban</h2>
      <span class="fermented__type-rule fermented__type-rule--above"></span>
      <p class="fermented__type">Fermented milk</p>
      <span class="fermented__type-rule fermented__type-rule--below"></span>
      <p class="fermented__note">Fenugreek added to enhance flavour</p>
      <span class="fermented__volume">1.5 L</span>
    </div>
  </section>

  <section class="label label--organic">
    <svg class="label__shapes" viewBox="0 0 340 430" preserveAspectRatio="none" aria-hidden="true">
      <path fill="var(--foam)" d="M200 0 H340 V84 C330 70 322 50 306 40 C290 30 274 34 262 24 C250 14 240 6 200 0 Z"/>
    </svg>
    <div class="label__content">
      <span class="badge"></span>
      <div class="camel-art" role="img" aria-label="Golden silhouette of a camel"></div>
      <h2 class="organic__name">Laban</h2>
      <p class="organic__tagline">Organic camel based milk</p>
      <div class="organic__splash" role="img" aria-label="Milk splash with small camels leaping through it"></div>
      <p class="organic__note">Fenugreek added to enhance flavour</p>
      <p class="organic__volume">1.5 L</p>
    </div>
  </section>

</main>
</body>
</html>
```